reminder mailer cards

redesign the reminder back cards , the cards are four to a standard sheet of card stock 8.5" x 11" expires 12/31/2020 replace ( across from meridale) with ( next to Penny Larder)

Font styles to use
Sans Serif

```html
<!DOCTYPE html>
<html lang="en">
<head>
<meta charset="utf-8">
<title>Swift Lube Reminder Card</title>
<link href="https://fonts.googleapis.com/css2?family=Exo+2:ital,wght@0,500;0,700;1,700;1,800&display=swap" rel="stylesheet">
<style>
  :root {
    --ink: #000000;
    --red: #e60005;
    --white: #ffffff;
    --page: #ffffff;
  }
  * { box-sizing: border-box; margin: 0; padding: 0; }
  html, body {
    width: 1200px; height: 1000px; overflow: hidden;
    background: var(--page);
    font-family: "Exo 2", Arial, sans-serif;
  }
  .card {
    position: absolute; left: 250px; top: 217px;
    width: 708px; height: 566px;
    background: var(--white);
  }
  .band { position: absolute; left: 0; width: 100%; }
  .band--brand { top: 0; height: 108px; background: var(--ink); }
  .band--offer { top: 111px; height: 302px; background: var(--red); }
  .band--info  { top: 416px; height: 102px; background: var(--ink); }
  .band--footer{ top: 521px; height: 45px; background: var(--red); }

  .brand-name {
    position: absolute; left: 30px; top: 24px;
    font-size: 60px; font-weight: 700; letter-spacing: 3px;
    color: var(--red); line-height: 1;
  }

  .service-art {
    position: absolute; left: 0; top: 0; width: 455px; height: 302px;
    background: linear-gradient(90deg, #f2f2f2 0%, #8a1a1c 35%, #1a1a1a 55%, var(--red) 100%);
  }

  .offer-title {
    position: absolute; left: 486px; top: 8px;
    color: var(--white); font-weight: 800; font-style: italic;
    font-size: 38px; line-height: 46px;
  }
  .offer-save {
    position: absolute; left: 462px; top: 100px;
    width: 246px; height: 123px;
  }
  .offer-save svg { position: absolute; inset: 0; }
  .offer-save p {
    position: relative; color: var(--red); font-weight: 800; font-style: italic;
    line-height: 1; padding-left: 38px;
  }
  .offer-save .save-word { font-size: 50px; padding-top: 6px; }
  .offer-save .save-amount { font-size: 58px; padding-left: 28px; }
  .offer-detail {
    position: absolute; left: 463px; top: 232px;
    color: var(--white); font-weight: 700; font-size: 23px; line-height: 32px;
  }

  .info-row {
    position: absolute; display: flex; align-items: center; gap: 8px;
    color: var(--white); font-weight: 500; font-size: 19px;
  }
  .info-row svg { width: 19px; height: 19px; flex: none; }
  .info-address { left: 40px; top: 20px; }
  .info-phone { left: 535px; top: 20px; }
  .info-hours { left: 40px; top: 64px; }

  .footer-perk {
    position: absolute; left: 68px; top: 10px;
    color: var(--white); font-weight: 700; font-style: italic; font-size: 20px;
  }
  .footer-expiry {
    position: absolute; left: 482px; top: 10px;
    color: var(--white); font-weight: 500; font-size: 20px;
  }
</style>
</head>
<body>
<main class="card">
  <header class="band band--brand">
    <h1 class="brand-name">SWIFT LUBE</h1>
  </header>

  <section class="band band--offer">
    <div class="service-art" role="img" aria-label="Illustration of a car with its hood open beside an oil bottle and wrench icon on a halftone dot background"></div>
    <h2 class="offer-title">Express<br>Lube</h2>
    <div class="offer-save">
      <svg viewBox="0 0 246 123" preserveAspectRatio="none" aria-hidden="true">
        <polygon points="20,0 246,0 246,123 0,123" fill="#ffffff"/>
      </svg>
      <p class="save-word">SAVE</p>
      <p class="save-amount">$5.00!</p>
    </div>
    <p class="offer-detail">9 Minute, 14 Point<br>Complete Service</p>
  </section>

  <section class="band band--info">
    <p class="info-row info-address">
      <svg viewBox="0 0 20 20" aria-hidden="true"><circle cx="10" cy="10" r="10" fill="#e60005"/><path d="M10 4a4 4 0 0 0-4 4c0 3 4 8 4 8s4-5 4-8a4 4 0 0 0-4-4z" fill="#fff"/><circle cx="10" cy="8" r="1.6" fill="#e60005"/></svg>
      48 Linden Road, Harlow (next to Penny Larder)
    </p>
    <p class="info-row info-phone">
      <svg viewBox="0 0 20 20" aria-hidden="true"><circle cx="10" cy="10" r="10" fill="#e60005"/><path d="M6.5 5l2 0 1 2.5-1.3 1a6 6 0 0 0 3.3 3.3l1-1.3 2.5 1 0 2c0 .6-.5 1-1 1A8.5 8.5 0 0 1 5.5 6c0-.5.4-1 1-1z" fill="#fff"/></svg>
      555-0148
    </p>
    <p class="info-row info-hours">
      <svg viewBox="0 0 20 20" aria-hidden="true"><circle cx="10" cy="10" r="10" fill="#e60005"/><circle cx="10" cy="10" r="5.5" fill="none" stroke="#fff" stroke-width="1.6"/><path d="M10 7v3.3l2 1.3" fill="none" stroke="#fff" stroke-width="1.5" stroke-linecap="round"/></svg>
      HOURS: MON-FRI 8am - 5pm, Sat 8am - 3pm
    </p>
  </section>

  <footer class="band band--footer">
    <p class="footer-perk">&gt; FREE Vacuum MON - FRI &lt;</p>
    <p class="footer-expiry">Expires 12/31/2020</p>
  </footer>
</main>
</body>
</html>
```